Business Card Re-Design for a Lighting Designer

I would like my business card re-designed. It is currently high gloss and they scratch too easily. I don not think the current design lends itself well to a matte finish. I have included the current design for reference along with our company logo.
Check out our website for current branding.
http://www.brambleorchidstudio.example

Updates
Some of the top contenders are muslim and it is a holiday for them. I do not want to discriminate and would expect the same courtesy for holidays we celebrate.
Target Market(s)
Interior Designers, Architects
Contact Information for Business Card
Logo - Name, Title, Address, Telephone Number and Extension, Email
Font styles to use
Requirements
Must have
- All the information listed on the current business card. If you use Red, it needs to be the red from our logo.
Nice to have
- Vertical and Horizontal Designs will be entertained.
Should not have
- Requirements for a glossy finish...should not look too corporate since we are a design firm.

```html
<!DOCTYPE html>
<html lang="en">
<head>
<meta charset="utf-8">
<title>Bramble Orchid Studio – Business Card</title>
<link rel="stylesheet" href="https://fonts.googleapis.com/css2?family=Cinzel:wght@700&family=Open+Sans:wght@400;600&display=swap">
<style>
  :root {
    --brand-red: #990000;
    --paper: #ffffff;
    --edge-grey: #999999;
    --ink: #111111;
    --backdrop: #f4f4f4;
    --card-w: 380px;
    --card-h: 665px;
    --stripe: 22px;
  }
  * { box-sizing: border-box; margin: 0; padding: 0; }
  html, body {
    width: 1200px; height: 1200px; overflow: hidden;
    background: var(--backdrop);
  }
  .sheet {
    width: 1200px; height: 1200px;
    display: flex; align-items: center; justify-content: center; gap: 160px;
  }
  .card {
    position: relative;
    width: var(--card-w); height: var(--card-h);
    display: flex; flex-direction: column; align-items: center;
    font-family: "Open Sans", sans-serif;
  }
  .card--front {
    background: var(--paper);
    border-left: var(--stripe) solid var(--brand-red);
    border-right: var(--stripe) solid var(--brand-red);
    justify-content: center;
  }
  .card--back {
    background: var(--brand-red);
    border-left: var(--stripe) solid var(--edge-grey);
    border-right: var(--stripe) solid var(--edge-grey);
    color: var(--paper);
    padding-top: 130px;
  }
  .wordmark {
    display: flex; align-items: center; gap: 12px;
    font-family: "Open Sans", sans-serif; font-weight: 400;
    line-height: 1.1;
  }
  .wordmark__square { flex: none; background: currentColor; }
  .card--front .wordmark { color: var(--ink); font-size: 34px; }
  .card--front .wordmark__square { width: 36px; height: 36px; color: var(--brand-red); background: var(--brand-red); }
  .card--back .wordmark { color: var(--paper); font-size: 24px; }
  .card--back .wordmark__square { width: 26px; height: 26px; }
  .wordmark__name { display: block; }
  .holder { margin-top: 110px; text-align: center; }
  .holder__name {
    font-family: "Cinzel", serif; font-weight: 700;
    font-size: 19px; letter-spacing: 0.3px;
  }
  .holder__title { font-size: 14px; font-weight: 600; margin-top: 2px; }
  .address {
    margin-top: 50px; text-align: center;
    font-size: 13.5px; font-weight: 600; line-height: 1.45;
  }
  .contacts { margin-top: 30px; list-style: none; font-size: 13.5px; font-weight: 600; line-height: 1.55; margin-left: 24px; }
  .contacts li { display: flex; align-items: center; gap: 7px; }
  .contacts svg { width: 12px; height: 12px; flex: none; }
</style>
</head>
<body>
<main class="sheet">
  <section class="card card--front" aria-label="Card front">
    <div class="wordmark">
      <span class="wordmark__square"></span>
      <span><span class="wordmark__name">Bramble</span><span class="wordmark__name">Orchid Studio</span></span>
    </div>
  </section>

  <section class="card card--back" aria-label="Card back">
    <div class="wordmark">
      <span class="wordmark__square"></span>
      <span><span class="wordmark__name">Bramble</span><span class="wordmark__name">Orchid Studio</span></span>
    </div>

    <div class="holder">
      <p class="holder__name">Marian Costello</p>
      <p class="holder__title">PRINCIPAL</p>
    </div>

    <p class="address">212 Linden Row Suite 40<br>Marlow, Oregon 97000 USA</p>

    <ul class="contacts">
      <li>
        <svg viewBox="0 0 12 12" aria-hidden="true"><path fill="#fff" d="M1 4c0-2 10-2 10 0v1H8V4H4v1H1zM3 6h6l1 5H2z"/><circle cx="6" cy="8.3" r="1.2" fill="#990000"/></svg>
        555.014.2290
      </li>
      <li>
        <svg viewBox="0 0 12 12" aria-hidden="true"><rect x="0.5" y="2.5" width="11" height="7" fill="#fff"/><path d="M0.5 2.5 6 7l5.5-4.5" fill="none" stroke="#990000" stroke-width="1"/></svg>
        info@brambleorchidstudio.example
      </li>
      <li>
        <svg viewBox="0 0 12 12" aria-hidden="true"><circle cx="6" cy="6" r="5.2" fill="none" stroke="#fff" stroke-width="1.2"/><path fill="#fff" d="M3 3.5 5.5 3 6 5 4.5 6.5 3.5 5zM7 7l2.5-.5L8.5 9.5 7 9z"/></svg>
        www.brambleorchidstudio.example
      </li>
    </ul>
  </section>
</main>
</body>
</html>
```